Lumen Vale Consulting business card

I have a new logo that was designed for me here on CraftHive. I am a medical device marketing consultant. The medical device industry is very professional, kind of dry, and can be a bit boring. But I'm in marketing so I want to look fresh and innovative, within the confines of the industry.

Please use the logo to its potential, making it colorful and visually interesting (I know, there's really only one color. I need some kind of interesting design element - maybe wraparound...

Target Market(s)

Marketing management in medical device companies.

Industry/Entity Type

Marketing

Requirements
Must have
• Melissa Corbin
Phone: 949-555-0143
Address: Harbor Glen, CA
melissa@lumenvaleconsulting.example
www.lumenvaleconsulting.example

```html
<!DOCTYPE html>
<html lang="en">
<head>
<meta charset="utf-8">
<title>Lumen Vale Consulting – Business Card</title>
<link href="https://fonts.googleapis.com/css2?family=Montserrat:wght@500;600;700&display=swap" rel="stylesheet">
<style>
  :root {
    --stage: #bdbec2;
    --card: #ffffff;
    --card-edge: #2b2b2b;
    --ink: #1a1a1a;
    --ink-soft: #3d3d3f;
    --grey: #7a7a7c;
    --sky: #4fc0ee;
    --sky-pale: #d8eefb;
  }
  * { box-sizing: border-box; margin: 0; padding: 0; }
  html, body { width: 1200px; height: 1196px; overflow: hidden; }
  body {
    background: var(--stage);
    font-family: "Montserrat", Arial, sans-serif;
    position: relative;
  }
  .card {
    position: absolute;
    width: 640px;
    height: 369px;
    background: var(--card);
    border: 2px solid var(--card-edge);
    border-radius: 48px;
    overflow: hidden;
  }
  .card--front { left: 283px; top: 197px; }
  .card--back { left: 291px; top: 628px; }

  .brand {
    position: absolute;
    left: 0; right: 0; top: 158px;
    display: flex;
    justify-content: center;
    align-items: center;
    gap: 16px;
  }
  .brand__dot {
    width: 26px; height: 26px;
    border-radius: 50%;
    background: var(--sky);
  }
  .brand__name {
    font-size: 40px;
    font-weight: 600;
    color: var(--ink-soft);
    letter-spacing: -0.5px;
  }

  .bloom {
    position: absolute;
    border-radius: 50%;
  }
  .bloom--corner-top {
    right: -70px; top: -70px;
    width: 220px; height: 220px;
    background: radial-gradient(circle, rgba(216,238,251,0.9) 0%, rgba(216,238,251,0.6) 55%, rgba(216,238,251,0) 72%);
  }
  .bloom--corner-bottom {
    left: -70px; bottom: -95px;
    width: 290px; height: 290px;
    background: radial-gradient(circle, rgba(120,200,240,0.55) 0%, rgba(190,228,249,0.55) 45%, rgba(216,238,251,0) 72%);
  }

  .person {
    position: absolute;
    left: 99px; top: 78px;
    font-weight: 700;
    font-size: 38px;
    line-height: 40px;
  }
  .person__first { color: var(--ink); display: block; }
  .person__last { color: var(--sky); display: block; padding-left: 36px; }

  .phone {
    position: absolute;
    left: 333px; top: 92px;
    display: flex; align-items: center; gap: 6px;
    font-size: 29px; font-weight: 700;
    color: var(--grey);
  }
  .phone svg { width: 36px; height: 42px; }

  .contacts {
    position: absolute;
    left: 203px; top: 200px;
    list-style: none;
  }
  .contacts li {
    display: flex; align-items: center;
    height: 31.5px;
    font-size: 16px; font-weight: 500;
    color: var(--ink);
  }
  .contacts svg { width: 22px; height: 22px; margin-right: 16px; flex: none; }
  .contacts .accent { color: var(--sky); }
</style>
</head>
<body>
  <section class="card card--front">
    <div class="brand">
      <span class="brand__dot"></span>
      <span class="brand__name">Lumen Vale Consulting</span>
    </div>
  </section>

  <section class="card card--back">
    <div class="bloom bloom--corner-top" role="img" aria-label="Soft pale-blue petal ornament in the corner"></div>
    <div class="bloom bloom--corner-bottom" role="img" aria-label="Soft light-blue petal ornament in the corner"></div>

    <h1 class="person">
      <span class="person__first">Melissa</span>
      <span class="person__last">Corbin</span>
    </h1>

    <div class="phone">
      <svg viewBox="0 0 24 28" aria-hidden="true">
        <path d="M7 2 C4 3 2 6 3 11 C5 18 10 24 15 26 C18 27 20 26 21 24 L17 19 C16 18 15 18 14 19 L12 20 C10 18 8 14 7 11 L9 10 C10 9 10 8 10 7 Z" fill="var(--grey)"/>
      </svg>
      <span>949-555-0143</span>
    </div>

    <ul class="contacts">
      <li>
        <svg viewBox="0 0 24 24" aria-hidden="true"><path d="M12 2 C7.6 2 5 5.2 5 9 C5 14 12 22 12 22 C12 22 19 14 19 9 C19 5.2 16.4 2 12 2 Z M12 12 A3 3 0 1 1 12 6 A3 3 0 1 1 12 12 Z" fill="var(--ink)" fill-rule="evenodd"/></svg>
        <span>Harbor Glen, CA</span>
      </li>
      <li>
        <svg viewBox="0 0 24 24" aria-hidden="true"><rect x="2" y="5" width="20" height="14" fill="var(--ink)"/><path d="M2 5 L12 13 L22 5" stroke="#fff" stroke-width="1.6" fill="none"/></svg>
        <span>melissa@lumenvaleconsulting.example</span>
      </li>
      <li>
        <svg viewBox="0 0 24 24" aria-hidden="true"><path d="M7 3 L7 20 L11 16 L14 22 L16.5 21 L13.5 15 L19 15 Z" fill="var(--ink)"/></svg>
        <span>www.<span class="accent">lumenvaleconsulting</span>.example</span>
      </li>
    </ul>
  </section>
</body>
</html>
```